Lantern Motion for Neighbors Business Cards

I need business cards for staff in a new startup. Our company name is Movrela - we train Tai Chi teachers. But our biggest project is called Lantern Motion for Neighbors - a federal project to put together free Tai Chi classes for Vets all across America. It's a young company, with a spirit of excitement, passion, a desire to do good for others (our Vets) and a modern style and sensibility. In other words, not old-fashioned Asian martial arts theme, but something new.

Industry/Entity Type

Health And Wellness

Contact Information for Business Card

The topic is ancient healing, but the company is the Pembrooks - so I'd like a card design that captures that.

Font styles to use
Sans Serif

Colors

Designer to choose colors to be used in the design.

Requirements
Nice to have
• I've got two logos - one for the company and one for the project. I want to see if we can incorporate them both without it becoming too busy.
Should not have
• Overly old-fashioned yin-yang themes.

```html
<!DOCTYPE html>
<html lang="en">
<head>
<meta charset="utf-8">
<title>Lantern Motion for Neighbors – Business Cards</title>
<link rel="stylesheet" href="https://fonts.googleapis.com/css2?family=Carlito:wght@400;700&display=swap">
<style>
  :root {
    --page-bg: #f1f1f1;
    --card-front-top: #d3d4d4;
    --card-front-bottom: #9c9c9c;
    --card-back: #ffffff;
    --ink: #7a7a7a;
    --ink-dark: #4a4a4a;
    --ink-faint: #c9c9c9;
    --mark-light: #ffffff;
    --tagline: #6f6f6f;
  }
  * { box-sizing: border-box; margin: 0; padding: 0; }
  html, body {
    width: 1200px; height: 1200px; overflow: hidden;
    background: var(--page-bg);
    font-family: "Carlito", "Calibri", sans-serif;
  }
  .sheet { position: relative; width: 1200px; height: 1200px; }
  .card {
    position: absolute; top: 276px;
    width: 368px; height: 628px;
    overflow: hidden;
  }
  .card-front {
    left: 198px;
    background: linear-gradient(180deg, var(--card-front-top) 0%, var(--card-front-bottom) 100%);
  }
  .card-back { left: 632px; background: var(--card-back); }

  .front-decor {
    position: absolute; left: 30px; top: 70px;
    width: 340px; height: 340px; border-radius: 50%;
    background: rgba(255,255,255,0.12);
  }
  .project-mark {
    position: absolute; left: 66px; top: 276px;
    display: flex; align-items: center; gap: 12px;
    color: var(--mark-light);
  }
  .project-mark .dot {
    width: 44px; height: 44px; border-radius: 50%;
    border: 2px solid var(--mark-light);
  }
  .project-mark .name { line-height: 1; }
  .project-mark .name-main { font-size: 24px; letter-spacing: 0.5px; display: block; }
  .project-mark .name-sub { font-size: 11px; letter-spacing: 2.2px; display: block; margin-top: 3px; }
  .tagline {
    position: absolute; left: 0; right: 0; top: 566px;
    text-align: center; font-size: 18px;
    letter-spacing: 7px; color: var(--tagline);
  }

  .contact {
    position: absolute; left: 65px; top: 244px;
    color: var(--ink); font-size: 19px; line-height: 24px;
  }
  .contact .gap { height: 22px; }
  .contact .phone { font-size: 14px; line-height: 20px; }
  .contact .email { font-size: 19px; }
  .company {
    position: absolute; right: 36px; top: 496px;
    text-align: right;
  }
  .company .intro { font-size: 13px; color: var(--ink-faint); }
  .company .mark {
    margin-top: 10px;
    display: flex; align-items: center; gap: 10px; justify-content: flex-end;
  }
  .company .mark .dot { width: 44px; height: 44px; border-radius: 50%; background: var(--ink-dark); }
  .company .mark .name { font-size: 24px; color: var(--ink-dark); }
</style>
</head>
<body>
<main class="sheet">
  <section class="card card-front">
    <div class="front-decor" aria-hidden="true"></div>
    <div class="project-mark">
      <span class="dot"></span>
      <span class="name">
        <span class="name-main">LANTERN MOTION</span>
        <span class="name-sub">FOR NEIGHBORS</span>
      </span>
    </div>
    <p class="tagline">mind · body · soul</p>
  </section>

  <section class="card card-back">
    <div class="contact">
      <p>Dana Whitlock</p>
      <p>1780 Harbor Crest Lane</p>
      <p>Raleigh NC, 27603</p>
      <div class="gap"></div>
      <p class="phone">555-014-2290</p>
      <p class="email">dwhitlock@movrela.com</p>
    </div>
    <div class="company">
      <p class="intro">an initiative by</p>
      <div class="mark">
        <span class="dot"></span>
        <span class="name">Movrela</span>
      </div>
    </div>
  </section>
</main>
</body>
</html>
```